Luxury Business Card Design for High-End Window Treatments

Gilded Slatworks
Custom Plantation Shutters & Architectural Shading Systems

⸻

BACK

Daniel Ferrowitz
Owner

Custom Interior & Exterior Window Treatments

919-555-0187
gildedslatworks.example

I have included a picture that I’m hoping we can use on the back, but I’m also wondering if you can get rid of the ladder? Should we get rid of shutters , shades and blinds underneath Gilded Slatworks?

Target Market(s)

High-end residential homeowners, custom home builders, architects, interior designers, and luxury renovation clients seeking premium plantation shutters and motorized architectural shading systems.

Industry/Entity Type

Custom Window treatments

Contact Information for Business Card

Front Gilded Slatworks Custom Plantation Shutters Motorized Architectural Shading Systems BACK Daniel Ferrowitz Owner 919-555-0187 GildedSlatworks.example Custom Interior & Exterior Window Treatments By Appointment

Requirements
Nice to have
• Not 100% sure on nice to halves or the color but you can definitely check out my website to get a better understanding of what I’m trying to do

```html
<!DOCTYPE html>
<html lang="en">
<head>
<meta charset="utf-8">
<title>Gilded Slatworks – Business Card</title>
<link rel="stylesheet" href="https://fonts.googleapis.com/css2?family=Poppins:wght@400;500;600&family=Cormorant+Garamond:wght@500&display=swap">
<style>
  :root {
    --stage: #b0b0b0;
    --cream: #e6ded0;
    --taupe: #b9b3a4;
    --charcoal: #2a2627;
    --ink: #2b2829;
    --photo-dark: #2b2f33;
    --photo-mid: #3c4047;
    --white: #ffffff;
  }
  * { box-sizing: border-box; margin: 0; padding: 0; }
  html, body { width: 1200px; height: 240px; overflow: hidden; }
  body {
    background: var(--stage);
    font-family: "Poppins", sans-serif;
    position: relative;
  }
  .card {
    position: absolute;
    top: 20px;
    width: 350px;
    height: 200px;
    border-radius: 34px;
    overflow: hidden;
  }
  .card--front { left: 225px; background: var(--cream); color: var(--ink); }
  .card--back { left: 625px; color: var(--white); }

  .wave { position: absolute; inset: 0; width: 100%; height: 100%; }

  .brand {
    position: absolute;
    left: 30px; top: 58px; width: 140px;
    text-align: center;
  }
  .brand__name {
    font-weight: 400;
    font-size: 16px;
    line-height: 19px;
    color: var(--ink);
  }
  .brand__services {
    margin-top: 4px;
    font-family: "Cormorant Garamond", serif;
    font-weight: 500;
    font-size: 8.5px;
    letter-spacing: .3px;
    word-spacing: 5px;
  }
  .divider {
    position: absolute;
    left: 175px; top: 54px;
    width: 1px; height: 67px;
    background: var(--ink);
    opacity: .6;
  }
  .contact { position: absolute; left: 200px; top: 50px; }
  .contact__name { font-weight: 600; font-size: 12.5px; line-height: 15px; }
  .contact__role { font-size: 6.5px; margin-top: 1px; opacity: .8; }
  .contact__tagline { font-weight: 500; font-size: 6px; line-height: 7.5px; margin-top: 7px; }
  .contact__list { list-style: none; margin-top: 9px; }
  .contact__item {
    display: flex; align-items: center; gap: 8px;
    font-weight: 500; font-size: 6.2px; line-height: 7.5px;
  }
  .contact__item svg { width: 5px; height: 5px; }

  .photo {
    position: absolute; inset: 0;
    background: linear-gradient(180deg, var(--photo-mid) 0%, var(--photo-dark) 55%, #24272a 100%);
  }
  .back__brand {
    position: absolute; left: 0; right: 0; top: 58px;
    text-align: center;
    font-weight: 400; font-size: 18px; line-height: 22px;
  }
  .back__tagline {
    position: absolute; left: 0; right: 0; top: 129px;
    text-align: center;
    font-size: 7.8px; line-height: 10px;
  }
</style>
</head>
<body>
  <section class="card card--front" aria-label="Card side with contact details">
    <svg class="wave" viewBox="0 0 350 200" preserveAspectRatio="none" aria-hidden="true">
      <path fill="var(--taupe)" d="M34 200 C70 150 120 138 160 148 C205 160 230 185 270 180 C310 175 335 150 350 126 L350 200 Z"/>
      <path fill="var(--cream)" d="M38 200 C74 158 122 148 160 156 C205 166 232 190 272 186 C312 182 336 158 350 132 L350 200 Z"/>
      <path fill="var(--charcoal)" d="M40 200 C78 168 124 160 162 168 C200 176 215 200 240 200 Z"/>
    </svg>
    <div class="brand">
      <p class="brand__name">Gilded<br>Slatworks</p>
      <p class="brand__services">Shutters Shades Blinds</p>
    </div>
    <div class="divider"></div>
    <div class="contact">
      <p class="contact__name">Daniel Ferrowitz</p>
      <p class="contact__role">Owner</p>
      <p class="contact__tagline">Custom Interior &amp;<br>Exterior Window Treatments</p>
      <ul class="contact__list">
        <li class="contact__item">
          <svg viewBox="0 0 10 10" aria-hidden="true"><path fill="var(--ink)" d="M2 0.5 L3.6 0.5 L4.3 2.8 L3.2 3.6 C3.8 5 4.9 6.2 6.4 6.8 L7.2 5.7 L9.5 6.4 L9.5 8 C9.5 9 8.8 9.5 8 9.5 C4 9.2 0.8 6 0.5 2 C0.5 1.2 1 0.5 2 0.5 Z"/></svg>
          919-555-0187
        </li>
        <li class="contact__item">
          <svg viewBox="0 0 10 10" aria-hidden="true"><g fill="none" stroke="var(--ink)" stroke-width="1.1"><circle cx="5" cy="5" r="4.2"/><ellipse cx="5" cy="5" rx="1.8" ry="4.2"/><path d="M0.8 5 H9.2"/></g></svg>
          gildedslatworks.example
        </li>
      </ul>
    </div>
  </section>

  <section class="card card--back" aria-label="Card side with brand and photo">
    <div class="photo" role="img" aria-label="Dusk photograph of a home's screened porch with white columns, darkened behind the text"></div>
    <p class="back__brand">Gilded<br>Slatworks</p>
    <p class="back__tagline">Custom Plantation Shutters &amp; Architectural<br>Shading Systems</p>
  </section>
</body>
</html>
```